Fern Guildworks Business Cards

Looking or a business card design for my start-up, called "Fern Guildworks".
Our tagline is "Growing the strength in every person through learning, craft, and community."
Our mission-driven work includes professional/personal development workshops, educational design services, organizational & project management consulting, and coaching services for K-12 schools, organizations, and individuals.
You can check out the website we're building at fernguildworks.com
I select projects from designers who are highly responsive to feedback, engage in dialog about revisions, and provide all root/source documents (so please state in your initial submission that you agree to do so).
Looking forward to seeing your great designs!!
Updates
Hello everyone,
Industry/Entity Type
Building
Requirements
Must have
- Looking for a two sided design that includes our logo (I am uploading two variations that I would like incorporated in .ai format) and website on both sides.
The front side must include:
Logo, Name, Title, Phone, Email, Twitter handle
The back side must include: Logo, @ferngild (our organizational twitter handle)
Nice to have
- I like the rounded corner business cards, but that is not absolutely essential.
Should not have
- Colors beyond those presented in our logo.

```html
<!DOCTYPE html>
<html lang="en">
<head>
<meta charset="utf-8">
<title>Fern Guildworks Business Cards</title>
<link href="https://fonts.googleapis.com/css2?family=Cinzel:wght@400&family=EB+Garamond:wght@400&display=swap" rel="stylesheet">
<style>
  :root {
    --stage: #2b2b2d;
    --card: #070707;
    --card-band: #121314;
    --sky: #6fcde3;
    --stone: #bdb6ad;
    --ink-light: #d6d6d6;
    --ink-muted: #9a9a9a;
  }
  * { margin: 0; padding: 0; box-sizing: border-box; }
  html, body {
    width: 1200px; height: 900px; overflow: hidden;
    background: var(--stage);
  }
  .stage { position: relative; width: 1200px; height: 900px; }

  .card {
    position: absolute;
    width: 560px; height: 320px;
    background: var(--card);
    border-radius: 14px;
    overflow: hidden;
    box-shadow: 0 20px 40px rgba(0,0,0,.55);
  }
  .card-band { position: absolute; inset: 0; }

  .card--back { left: 150px; top: 120px; }
  .card--front { left: 490px; top: 450px; }

  .brand {
    position: absolute;
    display: flex; align-items: center; gap: 14px;
  }
  .brand-dot {
    width: 22px; height: 22px; border-radius: 50%;
    background: var(--sky);
  }
  .brand-name {
    font-family: "Cinzel", serif;
    color: var(--stone);
    letter-spacing: .04em;
    white-space: nowrap;
  }

  .card--back .brand { left: 50%; top: 110px; transform: translateX(-50%); }
  .card--back .brand-name { font-size: 36px; }
  .tagline {
    position: absolute; left: 0; right: 0; top: 170px;
    text-align: center;
    font-family: "Cinzel", serif;
    font-size: 12.5px; letter-spacing: .14em; line-height: 1.5;
    color: var(--stone);
  }
  .card--back .website {
    position: absolute; left: 0; right: 0; top: 228px;
    text-align: center;
    font-family: "EB Garamond", serif;
    font-size: 19px; color: var(--sky);
  }

  .card--front .brand { left: 40px; top: 44px; }
  .card--front .brand-name { font-size: 28px; }
  .pillars {
    position: absolute; left: 76px; top: 86px;
    font-family: "Cinzel", serif;
    font-size: 10px; letter-spacing: .3em;
    color: var(--ink-muted);
    white-space: nowrap;
  }
  .card--front .website {
    position: absolute; left: 76px; top: 104px;
    font-family: "EB Garamond", serif;
    font-size: 10px; color: var(--ink-light);
  }
  .contact {
    position: absolute; left: 44px; top: 150px;
    font-family: "EB Garamond", serif;
  }
  .person-name { font-size: 26px; color: var(--sky); line-height: 1.1; }
  .person-title { font-size: 16px; color: var(--ink-light); margin-left: 8px; }
  .contact-lines {
    margin-top: 14px; margin-left: 10px;
    font-size: 17px; line-height: 1.25; color: var(--ink-light);
  }
  .contact-lines .label { color: var(--sky); }
  .follow {
    display: inline-flex; align-items: center; gap: 8px;
    margin-top: 6px; margin-left: 10px;
    padding: 3px 12px 3px 8px;
    background: var(--sky); border-radius: 6px;
    font-size: 17px; color: var(--card);
  }
  .follow-dot { width: 14px; height: 14px; border-radius: 50%; background: var(--card); }
</style>
</head>
<body>
<main class="stage">

  <section class="card card--back" aria-label="Card back">
    <svg class="card-band" width="560" height="320" viewBox="0 0 560 320" aria-hidden="true">
      <polygon points="0,200 170,320 0,320" fill="var(--card-band)"/>
    </svg>
    <div class="brand">
      <span class="brand-dot"></span>
      <span class="brand-name">Fern Guildworks</span>
    </div>
    <p class="tagline">Growing the strength in every person through<br>learning, craft, and community</p>
    <p class="website">www.fernguildworks.com</p>
  </section>

  <section class="card card--front" aria-label="Card front">
    <svg class="card-band" width="560" height="320" viewBox="0 0 560 320" aria-hidden="true">
      <polygon points="400,0 560,0 560,320 330,320" fill="var(--card-band)"/>
    </svg>
    <div class="brand">
      <span class="brand-dot"></span>
      <span class="brand-name">Fern Guildworks</span>
    </div>
    <p class="pillars">Learning | Craft | Community</p>
    <p class="website">www.fernguildworks.com</p>
    <div class="contact">
      <p class="person-name">Maren Holt</p>
      <p class="person-title">Owner</p>
      <p class="contact-lines">
        <span class="label">p:</span> 555 014 2290<br>
        <span class="label">e:</span> maren@fernguildworks.com
      </p>
      <p class="follow"><span class="follow-dot"></span>follow @ferngild</p>
    </div>
  </section>

</main>
</body>
</html>
```